Larkspur Homes - wanted BRILLIANT website design for our new property investing company

We need a website design for our new company based in Bristol, England, UK called "Larkspur Homes". We help buy people property who are in financial difficulty or who are needing to sell their property quickly for reasons such as death, divorce/separation, relocation, emigration.

We have a logo being designed incorporating strawberry and property (so red and green). We would like designs to communicate an elegant ,professional, approachable, friendly
fresh clean but also warm appealing appearance
Not too busy
Website consistent with logo and company name i.e. colour scheme

Please use our word document for content as a guide but use professional judgement for minor alterations if you feel they would benefit the site/structure etc

Please ask at any time if not sure

Target Market(s)

Adult british population, those that have a mortgage / loan / own property

Industry/Entity Type

Financial

Font styles to use
Serif
Sans Serif
Decorative

Colors
0692cd
33b7a4
acd036
fbee3e
3176b5
886aae
a6479a
e567a6
eb1f27

Requirements
Must have
• This must not look like a template website we are looking for UNIQUE please!
Nice to have
• Bristol pictures instead of generic, or colourful line drawings/comic drawings of houses/property/keys/happy people.....
Should not have
• An obvious off the shelf template design

```html
<!DOCTYPE html>
<html lang="en">
<head>
<meta charset="utf-8">
<title>Larkspur Homes</title>
<link href="https://fonts.googleapis.com/css2?family=Figtree:wght@300;400;600;700&family=Open+Sans:ital,wght@0,400;0,600;0,700;1,400&display=swap" rel="stylesheet">
<style>
:root{
  --green:#3f9442;
  --green-dark:#2f8532;
  --green-deep:#1e5c21;
  --green-text:#3a8f3d;
  --red:#a52a2a;
  --grey-bg:#f0f0f0;
  --bar-bg:#f3f3f3;
  --text:#555;
  --footer:#2b2b2b;
  --footer-text:#cfcfcf;
  --copy-bg:#c9c9c9;
}
*{margin:0;padding:0;box-sizing:border-box}
html,body{width:830px;height:1200px;overflow:hidden}
body{position:relative;background:#fff;font-family:"Figtree",sans-serif;color:var(--text)}
.abs{position:absolute}
/* top bar */
.topbar{left:0;top:0;width:830px;height:34px;background:var(--bar-bg);font-size:10px;color:#777}
.topbar .contact{left:70px;top:11px}
.topbar .contact span{margin-right:16px}
.social{right:80px;top:10px;display:flex;gap:14px}
.social i{display:block;width:12px;height:12px;border-radius:50%;background:#c4c4c4}
/* header */
.brand{left:73px;top:50px;width:120px;font-family:"Open Sans",sans-serif;font-weight:700;font-size:20px;line-height:25px;color:#555}
.nav{left:218px;top:62px;display:flex;align-items:center;font-size:10.4px;color:#666}
.nav a{text-decoration:none;color:inherit;margin-right:27px}
.nav a.active{color:var(--green-text);border:1.5px solid #ddd;border-radius:12px;padding:5px 15px;margin-right:13px}
/* hero */
.hero-text{left:0;top:120px;width:386px;height:287px;background:var(--green);color:#fff;padding:38px 0 0 81px}
.hero-text h1{font-size:24px;font-weight:300;line-height:30px;margin-bottom:17px}
.hero-text h1 b{font-weight:700}
.hero-text p{width:260px;font-size:10.4px;line-height:15.2px;margin-bottom:9px}
.btn-outline{display:inline-block;margin-top:16px;width:90px;height:30px;border:2px solid #fff;border-radius:15px;font-size:11px;text-align:center;line-height:26px}
.hero-photo{left:386px;top:120px;width:444px;height:287px;background:linear-gradient(160deg,#2a3f6e 0%,#4a4a5c 30%,#b0782e 55%,#e0a24a 70%,#3f6f96 100%)}
/* reasons */
.reasons{left:0;top:407px;width:386px;height:84px;background:var(--green-dark);display:flex;padding-left:73px}
.reason{width:77px;height:84px;text-align:center;color:#fff;font-size:10px;position:relative;border-right:1px solid rgba(255,255,255,.15)}
.reason:last-child{border-right:0}
.reason svg{display:block;margin:14px auto 4px}
.marker{left:108px;top:410px;width:0;height:0;border-left:4px solid transparent;border-right:4px solid transparent;border-bottom:6px solid #fff}
/* testimonial */
.quote{left:386px;top:407px;width:444px;height:84px;border-bottom:2px solid #e6e6e6}
.quote .mark{font-family:"Open Sans",sans-serif;font-weight:700;font-size:40px;color:#999;line-height:1}
.quote .body{position:absolute;left:49px;top:14px;width:305px}
.quote p{font-size:10.2px;line-height:14px;color:#888}
.quote .who{margin-top:6px;font-size:10.2px;color:var(--green-text)}
/* intro band */
.band{left:0;top:493px;width:830px;height:381px;background:var(--grey-bg)}
.lead{left:0;top:30px;width:830px;text-align:center;font-size:15px;line-height:22px;color:#555}
.card{top:97px;width:216px;height:244px;background:#fff;box-shadow:0 1px 3px rgba(0,0,0,.15);border-radius:2px}
.card h2{position:absolute;left:16px;top:13px;font-size:13.6px;font-weight:400;color:#444}
.card .rule{position:absolute;left:16px;right:16px;height:0;border-top:1px dotted #aac4e4}
.card ul{position:absolute;left:16px;top:48px;width:190px;list-style:none;font-family:"Open Sans",sans-serif;font-size:8.6px;line-height:13.8px;color:#888}
.card li{padding-left:7px;position:relative}
.card li::before{content:"";position:absolute;left:0;top:5.5px;width:3px;height:3px;border-radius:50%;background:#aaa}
.btn-red{position:absolute;top:214px;height:19px;background:var(--red);color:#fff;font-size:9.8px;text-align:center;line-height:19px;border-radius:1px}
.field{position:absolute;left:16px;width:186px;height:21px;border:1px solid #ddd;box-shadow:inset 0 2px 2px rgba(0,0,0,.08);font-family:"Open Sans",sans-serif;font-size:8.6px;color:#aaa;padding:5px 6px}
/* partners */
.partners{left:0;top:874px;width:830px;height:78px;display:flex;align-items:center;justify-content:space-around;padding:0 70px}
.partners i{display:block;width:92px;height:16px;border-radius:3px;background:#dcdcdc}
.partners i.dark{background:#9aa6b5}
/* footer */
.footer{left:0;top:952px;width:830px;height:207px;background:var(--footer);color:var(--footer-text)}
.footer h3{position:absolute;top:29px;font-size:11.6px;font-weight:400;color:#fff}
.footer .divider{position:absolute;top:18px;width:1px;height:170px;background:#3a3a3a}
.post-title{position:absolute;left:95px;font-family:"Open Sans",sans-serif;font-weight:700;font-size:7.8px;color:#fff}
.date{position:absolute;width:30px;height:30px;background:#1c1c1c;text-align:center;color:#fff;font-family:"Open Sans",sans-serif}
.date small{display:block;font-size:5.6px;padding-top:4px;font-style:italic}
.date b{display:block;font-size:13px;font-weight:400;font-style:italic;line-height:13px}
.post-text{position:absolute;left:131px;width:140px;font-family:"Open Sans",sans-serif;font-size:7.4px;line-height:10.6px}
.post-text u{font-weight:700;color:#fff}
.event{position:absolute;left:359px;font-family:"Open Sans",sans-serif;font-style:italic;font-size:11px;color:#fff}
.event-time{position:absolute;left:359px;font-family:"Open Sans",sans-serif;font-size:5.6px}
.event-time::before{content:"";display:inline-block;width:5px;height:5px;border:1px solid #ccc;border-radius:50%;margin-right:3px;vertical-align:-1px}
.about{position:absolute;left:501px;width:246px;font-family:"Open Sans",sans-serif;font-size:8px;line-height:12.4px}
.copyright{left:0;top:1159px;width:830px;height:41px;background:var(--copy-bg);text-align:center;line-height:41px;font-size:9.2px;color:#222}
</style>
</head>
<body>

<div class="abs topbar">
  <div class="abs contact"><span>Call Us : 0800 555 0192</span><span>Email : hello@larkspurhomes.co.uk</span></div>
  <div class="abs social" aria-label="Social links"><i></i><i></i><i></i><i></i><i></i><i></i></div>
</div>

<div class="abs brand">Larkspur Homes</div>
<nav class="abs nav">
  <a class="active" href="#">Home</a>
  <a href="#">Sell your property fast</a>
  <a href="#">Rent Your property fast</a>
  <a href="#">The 5 easy step</a>
  <a href="#">About Us</a>
  <a href="#">Contact Us</a>
</nav>

<section class="abs hero-text">
  <h1><b>Larkspur</b> Homes</h1>
  <p>Lorem ipsum dolor sit amet, consectetur adipisicing elit, sed do eiusmod tempor incididunt ut labore et dolore magna aliqua. Ut enim ad minim veniam, quis nostrud exercitation ullamco laboris nisi ut aliquip ex ea commodo consequat.</p>
  <p>Duis aute irure dolor in reprehenderit in voluptate velit esse cillum dolore eu fugiat nulla pariatur.</p>
  <div class="btn-outline">Read More</div>
</section>
<div class="abs hero-photo" role="img" aria-label="Photo of a modern house lit at dusk beside a swimming pool"></div>

<div class="abs reasons">
  <div class="reason">
    <svg width="48" height="48" viewBox="0 0 48 48"><circle cx="24" cy="24" r="24" fill="var(--green-deep)"/><path d="M22 12h4v7h7v4h-7v9h-4v-9h-7v-4h7z" fill="#fff"/><rect x="15" y="33" width="18" height="3" fill="#fff"/></svg>Death
  </div>
  <div class="reason">
    <svg width="48" height="48" viewBox="0 0 48 48"><circle cx="24" cy="24" r="24" fill="var(--green-deep)"/><path d="M24 11l-12 11h3v13h18V22h3z" fill="#fff"/><path d="M24 14l-2 6 3 4-2 5 1 6" stroke="var(--green-deep)" stroke-width="1.6" fill="none"/><rect x="17" y="25" width="4" height="4" fill="var(--green-deep)"/><rect x="27" y="25" width="4" height="4" fill="var(--green-deep)"/></svg>Divorce
  </div>
  <div class="reason">
    <svg width="48" height="48" viewBox="0 0 48 48"><circle cx="24" cy="24" r="24" fill="var(--green-deep)"/><path d="M18 20a9 9 0 1 1 4 14" stroke="#fff" stroke-width="4" fill="none"/><path d="M12 13l9 2-6 8z" fill="#fff"/></svg>Relocation
  </div>
  <div class="reason">
    <svg width="48" height="48" viewBox="0 0 48 48"><circle cx="24" cy="24" r="24" fill="var(--green-deep)"/><rect x="14" y="13" width="8" height="7" rx="1" fill="#fff"/><rect x="24" y="22" width="12" height="13" rx="1.5" fill="#fff"/><path d="M27 22v-3h6v3" stroke="#fff" stroke-width="1.6" fill="none"/><path d="M15 22h6v13h-6z" fill="#fff"/></svg>Emigration
  </div>
</div>
<div class="abs marker"></div>

<section class="abs quote">
  <span class="abs mark" style="left:20px;top:13px">&ldquo;</span>
  <div class="body">
    <p>Lorem Ipsum is simply dummy text of the printing and typesetting industry. Lorem Ipsum has been the industry's 1500s.</p>
    <div class="who">Maren Holt, CEO</div>
  </div>
  <span class="abs mark" style="left:330px;top:40px">&rdquo;</span>
</section>

<section class="abs band">
  <div class="abs lead">Do you want to sell or rent out your house quickly? Lorem ipsum dolor<br>Dolor sit amet consectetur adipsicing elit sed do euismod tempor incidunt magna aliqua</div>

  <div class="abs card" style="left:69px">
    <h2>Who specialize in:</h2>
    <div class="rule" style="top:35px"></div>
    <ul>
      <li>Buying Properties Quickly</li>
      <li>Finding Creative Solutions To Your Property Problems</li>
      <li>Property Rental Management</li>
      <li>Lettings To Professional &amp; Student Tenants</li>
      <li>Guaranteed Rent &amp; Management Schemes For Landlords</li>
      <li>STOPPING Repossessions</li>
      <li>Motivated Sellers</li>
      <li>Chain Fixing</li>
      <li>Negative Equity Problems</li>
    </ul>
    <div class="rule" style="top:204px"></div>
    <div class="btn-red" style="left:16px;width:57px">View all</div>
  </div>

  <div class="abs card" style="left:307px">
    <h2>Who can we help?</h2>
    <div class="rule" style="top:35px"></div>
    <ul>
      <li>How to stop repossession</li>
      <li>Divorce or Sepration</li>
      <li>Financial Problems</li>
      <li>Dont Like Estate Agents</li>
      <li>Property needing work</li>
      <li>Retiring landlords</li>
      <li>Negative Equity</li>
      <li>Opportunity not to be missed!!</li>
      <li>Guranteed rent Scheme</li>
      <li>Ill Health</li>
      <li>Relocating</li>
    </ul>
    <div class="rule" style="top:204px"></div>
    <div class="btn-red" style="left:16px;width:57px">View all</div>
  </div>

  <div class="abs card" style="left:545px">
    <h2>Contact Form:</h2>
    <div class="rule" style="top:35px"></div>
    <div class="field" style="top:47px">Name</div>
    <div class="field" style="top:74px">Email</div>
    <div class="field" style="top:101px">Phone Number</div>
    <div class="field" style="top:128px">Address Location</div>
    <div class="field" style="top:155px;height:50px">Message</div>
    <div class="btn-red" style="left:146px;width:56px">Submit</div>
  </div>
</section>

<div class="abs partners" aria-label="Partners"><i></i><i></i><i></i><i></i><i class="dark"></i></div>

<footer class="abs footer">
  <h3 style="left:94px">NEWS AND ARTICLES</h3>
  <div class="divider" style="left:298px"></div>
  <h3 style="left:318px">EVENTS</h3>
  <div class="divider" style="left:486px"></div>
  <h3 style="left:501px">WHAT WE DO</h3>

  <div class="post-title" style="top:61px">Space Ipsum</div>
  <div class="date" style="left:95px;top:80px"><small>MAR</small><b>23</b></div>
  <div class="post-text" style="top:80px">Astronomy compels the soul to look upward, and leads us from this world to another. There ... <u>More</u></div>
  <div class="post-title" style="top:128px">This Is A Post</div>
  <div class="date" style="left:95px;top:147px"><small>MAR</small><b>23</b></div>
  <div class="post-text" style="top:147px">Here men from the planet Earth first set foot upon the Moon. July 1969 AD. We came in peac... <u>More</u></div>

  <div class="date" style="left:318px;top:64px"><small>APR</small><b>27</b></div>
  <div class="event" style="top:62px">Ellis Marsh Seminar</div>
  <div class="event-time" style="top:80px">00:00 AM - 00:00 AM</div>
  <div class="date" style="left:318px;top:108px"><small>AUG</small><b>31</b></div>
  <div class="event" style="top:106px">Corwin Self Defense</div>
  <div class="event-time" style="top:124px">00:00 AM - 00:00 AM</div>
  <div class="date" style="left:318px;top:152px"><small>JUN</small><b>07</b></div>
  <div class="event" style="top:150px">Tilda's Boxercise</div>
  <div class="event-time" style="top:168px">00:00 AM - 00:00 AM</div>

  <p class="about" style="top:59px">Ma quande lingues coalesce, li grammatica del resultant lingue es plu simplic e regulari quam ti del coalescent lingues. Li nov lingua franca va esser plu simplic e regulari quam li existent Europan lingues.</p>
  <p class="about" style="top:123px">It va esser tam simplic quam Occidental: in fact, it va esser Occidental. A un Angleso it va semblar un simplificat Angles, quam.</p>
</footer>

<div class="abs copyright">&copy; Copyright Larkspur Homes 2014 All Rights Reserved</div>

</body>
</html>
```